Bramblewick Co Leaflet. A5 2-sided Flyer for a UK Lawn Treatment Company

I need an A5 two-side leaflet / flyer designed for my Lawn Treatment company. The leaflet will be for door-drops so quick impact needed. Full colour, both sides. I provide lawn treatments to customers in the Exeter area of Devon. I would like to design to be clear, fresh and reflect the joy a good lawn and garden can bring.

Target Market(s)

Home Owners. 30-80 Years. Familys

Font styles to use
Sans Serif

Colors
9bcb3c
f78f20
ec1f27
33a6d7

Requirements
Must have
• Good front page picture
• Logo
• Contact details on front.
• Call to Action
• More details in Text file included in design.
Nice to have
• Clipart of a family / lady enjoying a lawn.

```html
<!DOCTYPE html>
<html lang="en">
<head>
<meta charset="utf-8">
<title>Bramblewick Co Leaflet</title>
<link href="https://fonts.googleapis.com/css2?family=Fira+Sans:wght@700&family=Oswald:wght@500;600&family=Roboto+Slab:wght@400&family=Kaushan+Script&display=swap" rel="stylesheet">
<style>
:root{
  --stage:#e4e6e3;
  --deep-green:#0f4a2a;
  --leaf-green:#3bb54a;
  --text-green:#198a3c;
  --lawn-light:#cfe3a1;
  --sun-yellow:#fbb817;
  --alert-red:#d42a1d;
  --sky-blue:#2a7fc1;
  --ink:#2b2b2b;
  --white:#ffffff;
}
*{margin:0;padding:0;box-sizing:border-box}
html,body{width:1200px;height:908px;overflow:hidden;background:var(--stage)}
.canvas{position:relative;width:1200px;height:908px}
.page{position:absolute;top:53px;width:528px;height:745px;overflow:hidden;background:var(--white);box-shadow:0 4px 18px rgba(0,0,0,.18)}
.page--front{left:49px}
.page--back{left:614px}
.page svg.bg{position:absolute;left:0;top:0}
.abs{position:absolute;white-space:nowrap}
.brand{display:flex;align-items:center;gap:8px;font-family:"Roboto Slab",serif;color:var(--deep-green);font-size:22px;line-height:1}
.brand__dot{width:14px;height:14px;border-radius:50%;background:var(--leaf-green)}
.front-brand{left:18px;top:88px}
.back-brand{left:0;width:528px;justify-content:center;top:86px;font-size:26px}
.hero{left:110px;width:430px;text-align:center;font-family:"Fira Sans",sans-serif;font-weight:700;color:var(--white);text-shadow:0 2px 4px rgba(0,0,0,.45);line-height:1}
.hero__lead{top:128px;font-size:22px}
.hero__accent{top:152px;font-size:39px;color:var(--sun-yellow)}
.hero__main{top:194px;font-size:39px;letter-spacing:-.3px}
.intro{right:21px;top:578px;text-align:right;font-family:"Roboto Slab",serif;color:var(--white);font-size:19px;line-height:22px}
.intro__title{color:var(--sun-yellow);font-size:21px;margin-bottom:1px}
.contact{left:0;top:682px;width:528px;height:63px;background:var(--sun-yellow);font-family:"Roboto Slab",serif;font-size:13px;color:var(--ink)}
.contact__tab{position:absolute;left:0;top:-19px;height:26px;padding:2px 14px;background:var(--sun-yellow);border-radius:0 6px 0 0;font-family:"Kaushan Script",cursive;font-size:16px;color:var(--deep-green)}
.contact__rows{position:absolute;left:23px;top:11px;display:grid;grid-template-columns:88px auto;line-height:16px}
.contact .lbl{color:var(--alert-red)}
.headline{left:31px;top:150px;font-family:"Oswald",sans-serif;font-weight:600;font-size:25px;line-height:30px;color:var(--sun-yellow);letter-spacing:-.4px}
.body{font-family:"Roboto Slab",serif;font-size:12.2px;line-height:15.4px;color:var(--ink);text-align:justify;white-space:normal}
.body--intro{left:31px;top:181px;width:466px}
.section{left:21px;width:487px;white-space:normal}
.section h3{font-family:"Roboto Slab",serif;font-weight:400;font-size:14px;line-height:16px;margin-bottom:0}
.section--understand{top:384px}
.section--understand h3{color:var(--alert-red)}
.section--treatments{top:454px}
.section--treatments h3{color:var(--text-green)}
.section--industry{top:523px}
.section--industry h3{color:var(--sky-blue)}
.services{left:25px;top:578px;list-style:none;font-family:"Roboto Slab",serif;font-size:12.5px;line-height:15.6px;color:var(--text-green)}
.services li::before{content:"";display:inline-block;border-left:5px solid var(--alert-red);border-top:4px solid transparent;border-bottom:4px solid transparent;margin-right:6px}
.cta{left:234px;top:607px;width:272px;height:102px;background:var(--sun-yellow);border-radius:6px;padding:5px 8px;font-family:"Roboto Slab",serif;color:var(--ink);white-space:normal}
.cta__lead{font-family:"Kaushan Script",cursive;font-size:10.5px;line-height:13px;text-align:center;white-space:nowrap}
.cta__phone{font-family:"Oswald",sans-serif;font-weight:600;font-size:22px;color:var(--text-green);text-align:center;line-height:30px;letter-spacing:-.5px;white-space:nowrap}
.cta__phone span{color:var(--alert-red)}
.cta__label{font-size:8.5px;line-height:11px;margin-top:4px}
.cta__quote{font-family:"Kaushan Script",cursive;font-size:7px;line-height:12px}
.cta__quote em{font-style:normal;color:var(--alert-red)}
</style>
</head>
<body>
<main class="canvas">

  <section class="page page--front">
    <svg class="bg" width="528" height="745" viewBox="0 0 528 745">
      <defs>
        <linearGradient id="gardenTone" x1="0" y1="0" x2="1" y2="1">
          <stop offset="0" stop-color="#4c7a32"/>
          <stop offset=".45" stop-color="#2f6a22"/>
          <stop offset="1" stop-color="#5aa02c"/>
        </linearGradient>
        <radialGradient id="terraceTone" cx=".5" cy=".4" r=".6">
          <stop offset="0" stop-color="#6ba03a"/>
          <stop offset="1" stop-color="#2c5a22"/>
        </radialGradient>
      </defs>
      <g role="img" aria-label="Photo of a striped green lawn and gravel path beside a white garden gazebo">
        <path d="M0 310 C150 160 340 60 528 18 L528 682 L0 682 Z" fill="url(#gardenTone)"/>
      </g>
      <path d="M0 310 C150 160 340 60 528 18" fill="none" stroke="var(--leaf-green)" stroke-width="14"/>
      <path d="M0 560 C200 560 420 500 528 392 L528 682 L0 682 Z" fill="var(--deep-green)"/>
      <path d="M0 560 C200 560 420 500 528 392" fill="none" stroke="var(--leaf-green)" stroke-width="8"/>
      <path d="M353 243 q22 14 44 0" fill="none" stroke="#fff" stroke-width="4" stroke-linecap="round"/>
      <circle cx="375" cy="425" r="125" fill="url(#terraceTone)" stroke="var(--leaf-green)" stroke-width="9" role="img" aria-label="Photo of a garden terrace with lawn and woodland"/>
      <circle cx="129" cy="587" r="55" fill="#1f6b33" stroke="#6cbf45" stroke-width="3"/>
      <circle cx="129" cy="587" r="42" fill="none" stroke="#6cbf45" stroke-width="2"/>
    </svg>

    <div class="abs brand front-brand"><span class="brand__dot"></span>Bramblewick Co</div>

    <p class="abs hero hero__lead">Treatments and advice</p>
    <p class="abs hero hero__accent">TO KEEP YOUR</p>
    <p class="abs hero hero__main">LAWN LOOKING NICE</p>

    <div class="abs intro">
      <p class="intro__title">BRAND NEW TO THE AREA!</p>
      <p>8 Years experience maintaining<br>the finest lawns of Cheshire</p>
    </div>

    <div class="abs contact">
      <span class="contact__tab">Contact Us</span>
      <div class="contact__rows">
        <span class="lbl">Call today on</span><span>: 01632 960418 or <span class="lbl">Text</span> : 07700 900527 to book your lawn survey</span>
        <span class="lbl">website</span><span>: bramblewickco.co.uk</span>
      </div>
    </div>
  </section>

  <section class="page page--back">
    <svg class="bg" width="528" height="745" viewBox="0 0 528 745">
      <defs>
        <linearGradient id="freshWash" x1="0" y1="0" x2="0" y2="1">
          <stop offset=".15" stop-color="#ffffff"/>
          <stop offset="1" stop-color="#cfe3a1"/>
        </linearGradient>
        <radialGradient id="lawnTone" cx=".5" cy=".6" r=".6">
          <stop offset="0" stop-color="#7cc242"/>
          <stop offset="1" stop-color="#2f6a24"/>
        </radialGradient>
      </defs>
      <rect width="528" height="745" fill="url(#freshWash)"/>
      <path d="M0 0 H528 V102 C400 40 130 40 0 102 Z" fill="var(--deep-green)"/>
      <path d="M0 102 C130 40 400 40 528 102" fill="none" stroke="var(--leaf-green)" stroke-width="9"/>
      <circle cx="96" cy="306" r="66" fill="url(#lawnTone)" stroke="var(--leaf-green)" stroke-width="5" role="img" aria-label="Photo of a freshly striped lawn"/>
      <circle cx="263" cy="306" r="66" fill="url(#lawnTone)" stroke="var(--leaf-green)" stroke-width="5" role="img" aria-label="Photo of a lush lawn with shrubs"/>
      <circle cx="433" cy="306" r="66" fill="url(#lawnTone)" stroke="var(--leaf-green)" stroke-width="5" role="img" aria-label="Photo of a back garden lawn with flower pots"/>
      <rect y="722" width="528" height="23" fill="var(--deep-green)"/>
    </svg>

    <div class="abs brand back-brand"><span class="brand__dot"></span>Bramblewick Co</div>

    <h2 class="abs headline">FOR A BEAUTIFUL WEED-FREE LAWN</h2>
    <p class="abs body body--intro">Call Bramblewick Co today and start your journey to a wonderful, lush, green lawn you and your family can enjoy. Arrange a no-obligation lawn survey and quotation at a time to suit you. Call 01632 960418 now.</p>

    <div class="abs section section--understand">
      <h3>I WILL UNDERSTAND YOUR LAWN</h3>
      <p class="body">Every lawn is unique. I take time to gain a comprehensive understanding of your lawn and its situation. I will also listen to you and understand your problems and your aspirations for your grass.</p>
    </div>
    <div class="abs section section--treatments">
      <h3>YOUR LAWN TREATMENTS</h3>
      <p class="body">I will creat a custom treatment programme tailored to your lawn. I may also recommend some remedial treatments to correct any existing problems. There is no contract to sign. I guarantee all treatments.</p>
    </div>
    <div class="abs section section--industry">
      <h3>INDUSTRY-LEADING LAWN CARE</h3>
      <p class="body">I have 8 years of experience in the leading edge of domestic lawn care. I have a comprehensive range of treatments including:</p>
    </div>

    <ul class="abs services">
      <li>Scarification</li>
      <li>Aeration</li>
      <li>Moss Control</li>
      <li>Overseeding</li>
      <li>Top Dressing</li>
      <li>Lawn Repairs</li>
      <li>Fertilisation &amp; Weed Control</li>
      <li>Pest and Disease Management</li>
      <li>Special Event Preparation</li>
    </ul>

    <div class="abs cta">
      <p class="cta__lead">Save time and money and leave your lawn to an expert.</p>
      <p class="cta__phone">CALL <span>01632 960418</span> TODAY</p>
      <p class="cta__label">TESTIMONIALS</p>
      <p class="cta__quote">We have very much appreciated your service over the last four years, and especially value your reliability and perennial cheerfulness &nbsp;&nbsp;<em>-------- Marjorie</em></p>
    </div>
  </section>

</main>
</body>
</html>
```